Ridgeline Yard Works Stationary Package
Business Cards, Letterhead, Envelope, Sticker, Fax Cover sheet, invoice, and estimate
Ridgeline Yard Works Stationary Package - Construction
Creative Brief
Use same font as used in my logo
Pete Marrow
Owner
4172 W. Fenwick Rd. Burbank, IL 60421
petemarrow@quailnet.example
www.ridgelineyardworks.example
Can information be in a format that can be edited for future use. ex: Name Changes, New Numbers, etc?

```html
<!DOCTYPE html>
<html lang="en">
<head>
<meta charset="utf-8">
<title>Ridgeline Yard Works – Business Card</title>
<link rel="stylesheet" href="https://fonts.googleapis.com/css2?family=Exo+2:wght@500;600&family=Open+Sans:wght@400;600;700&display=swap">
<style>
  :root {
    --page: #ecebe8;
    --card: #ffffff;
    --navy: #1f2a7a;
    --blue: #2d5fc0;
    --red: #c4161c;
    --ink: #2b2b2b;
    --muted: #4a4a4a;
    --rule: #c9c9c9;
  }
  * { margin: 0; padding: 0; box-sizing: border-box; }
  html, body { width: 1200px; height: 778px; overflow: hidden; background: var(--page); }
  .canvas { position: relative; width: 1200px; height: 778px; }
  .business-card {
    position: absolute; left: 60px; top: 99px; width: 1080px; height: 580px;
    background: var(--card); border-radius: 36px; overflow: hidden;
    box-shadow: 0 6px 18px rgba(0,0,0,.18);
    font-family: "Open Sans", Arial, sans-serif; color: var(--ink);
  }
  .card-swooshes { position: absolute; inset: 0; }
  .brand { position: absolute; left: 70px; top: 52px; display: flex; align-items: center; gap: 34px; }
  .brand-square { width: 118px; height: 118px; background: var(--navy); border-radius: 18px; }
  .brand-text { display: flex; flex-direction: column; align-items: center; }
  .brand-name { font-family: "Exo 2", Arial, sans-serif; font-weight: 600; font-size: 64px; color: var(--navy); line-height: 1; letter-spacing: .5px; }
  .brand-tagline { margin-top: 12px; font-family: "Exo 2", Arial, sans-serif; font-weight: 500; font-size: 28px; color: var(--ink); }
  .owner { position: absolute; right: 702px; top: 300px; text-align: right; }
  .owner-name { font-size: 38px; font-weight: 600; color: var(--ink); }
  .owner-title { font-size: 28px; font-weight: 600; color: var(--muted); }
  .divider { position: absolute; left: 481px; top: 250px; width: 2px; height: 240px; background: var(--rule); }
  .address { position: absolute; left: 540px; top: 250px; font-size: 27px; line-height: 40px; color: var(--muted); }
  .contacts { position: absolute; left: 540px; top: 372px; list-style: none; font-size: 27px; line-height: 40px; color: var(--muted); }
  .contacts li { display: flex; align-items: center; gap: 14px; }
  .contacts svg { width: 22px; height: 22px; flex: none; }
</style>
</head>
<body>
<div class="canvas">
  <div class="business-card">
    <svg class="card-swooshes" viewBox="0 0 1080 580" preserveAspectRatio="none" aria-hidden="true">
      <defs>
        <linearGradient id="bandBlue" x1="0" y1="0" x2="1" y2="1">
          <stop offset="0" stop-color="#2d5fc0"/>
          <stop offset="1" stop-color="#1f2a7a"/>
        </linearGradient>
      </defs>
      <path d="M720 0 C900 40 1050 200 1080 560 L1080 0 Z" fill="var(--red)"/>
      <path d="M745 0 C915 38 1060 190 1080 500 L1080 0 Z" fill="url(#bandBlue)"/>
      <path d="M0 300 C70 420 170 520 270 580 L0 580 Z" fill="var(--red)"/>
      <path d="M0 330 C60 435 150 525 240 580 L0 580 Z" fill="url(#bandBlue)"/>
    </svg>

    <div class="brand">
      <div class="brand-square"></div>
      <div class="brand-text">
        <div class="brand-name">Ridgeline Yard Works</div>
        <div class="brand-tagline">Home Restoration Specialists</div>
      </div>
    </div>

    <div class="owner">
      <div class="owner-name">Pete Marrow</div>
      <div class="owner-title">Owner</div>
    </div>

    <div class="divider"></div>

    <div class="address">4172 W. Fenwick Rd.<br>Burbank, IL 60421</div>

    <ul class="contacts">
      <li>
        <svg viewBox="0 0 24 24"><path fill="var(--red)" d="M6 2h4l2 5-3 2a11 11 0 0 0 6 6l2-3 5 2v4a2 2 0 0 1-2 2A18 18 0 0 1 4 4a2 2 0 0 1 2-2z"/></svg>
        (708) 555-0148
      </li>
      <li>
        <svg viewBox="0 0 24 24"><rect x="6" y="1" width="12" height="22" rx="2" fill="var(--red)"/><rect x="8" y="4" width="8" height="13" fill="#fff"/></svg>
        (708) 555-0172
      </li>
      <li>
        <svg viewBox="0 0 24 24"><rect x="2" y="5" width="20" height="14" rx="1" fill="var(--red)"/><path d="M3 6l9 7 9-7" fill="none" stroke="#fff" stroke-width="2"/></svg>
        petemarrow@quailnet.example
      </li>
      <li>
        <svg viewBox="0 0 24 24"><circle cx="12" cy="12" r="10" fill="var(--red)"/><path d="M2 12h20M12 2c4 4 4 16 0 20M12 2c-4 4-4 16 0 20" fill="none" stroke="#fff" stroke-width="1.6"/></svg>
        www.ridgelineyardworks.example
      </li>
    </ul>
  </div>
</div>
</body>
</html>
```